Business card for Tolvery Anesthesia LLC

This is for a business care for Tolvery Anesthesia LLC. Dr. Lisbeth Tolvery, CRNA, DNAP is the sole provider in the LLC. Business address is 4718 N Brackley Street,
Oakhaven, PA 17342
CRNA stands for certified registered nurse anesthetist
"Keeping you safe and comfortable"
I plan to give this business card to the patients that I provide anesthesia to.
Creative design that ties into Anesthesia. Calm soothing colors.

Target Market(s)

Business card for my patients.

Industry/Entity Type

Medicine

Contact Information for Business Card

Creative, professional, eye catching

Logo Text

Tolvery Anesthesia

Font styles to use
Serif
Script

Colors

Designer to choose colors to be used in the design.

Requirements
Must have
• Tolvery Anesthesia
• Dr. Lisbeth Tolvery, CRNA, DNAP
• tolvery.anesthesia@ quillmail.net
Nice to have
• "Keeping you safe and comfortable"
Should not have
• phone number

```html
<!DOCTYPE html>
<html lang="en">
<head>
<meta charset="utf-8">
<title>Tolvery Anesthesia LLC — Business Card</title>
<link rel="stylesheet" href="https://fonts.googleapis.com/css2?family=Open+Sans:wght@400;700&family=Quicksand:wght@400&display=swap">
<style>
  :root {
    --page-bg: #e9e9ea;
    --card-bg: #f6f6f6;
    --back-bg: #d20051;
    --brand-magenta: #d4105f;
    --brand-deep: #a80f57;
    --on-back: #ffffff;
    --bloom-pale: #f3c8d9;
    --bloom-fade: rgba(243, 200, 217, 0);
  }
  * { margin: 0; padding: 0; box-sizing: border-box; }
  html, body {
    width: 1200px;
    height: 1200px;
    overflow: hidden;
    background: var(--page-bg);
  }
  .canvas {
    width: 1200px;
    height: 1200px;
    display: flex;
    flex-direction: column;
    align-items: center;
    justify-content: center;
    gap: 56px;
  }
  .business-card {
    position: relative;
    width: 900px;
    height: 514px;
    overflow: hidden;
    box-shadow: 0 2px 6px rgba(0, 0, 0, 0.12);
  }

  /* Back side */
  .card-back { background: var(--back-bg); }
  .back-content {
    position: absolute;
    left: 50%;
    top: 50%;
    transform: translate(-50%, -50%);
    text-align: center;
    color: var(--on-back);
  }
  .back-mark {
    display: block;
    margin: 0 auto;
    width: 110px;
    height: 110px;
  }
  .back-name {
    margin-top: 18px;
    font-family: "Open Sans", sans-serif;
    font-weight: 700;
    font-size: 28px;
    line-height: 1.25;
    letter-spacing: 4px;
    text-transform: uppercase;
  }

  /* Front side */
  .card-front { background: var(--card-bg); }
  .bloom-decoration {
    position: absolute;
    top: 0;
    right: 0;
    width: 310px;
    height: 514px;
    background: radial-gradient(ellipse 90% 70% at 78% 55%, var(--bloom-pale) 0%, rgba(243, 200, 217, 0.55) 45%, var(--bloom-fade) 80%);
  }
  .front-content {
    position: absolute;
    left: 303px;
    top: 0;
    width: 600px;
    height: 514px;
    transform: translateX(-50%);
    text-align: center;
    color: var(--brand-deep);
  }
  .front-content > * { position: absolute; left: 0; right: 0; }
  .brand-mark {
    top: 52px;
    width: 124px;
    height: 124px;
    margin: 0 auto;
  }
  .brand-name {
    top: 196px;
    font-family: "Open Sans", sans-serif;
    font-weight: 700;
    font-size: 27px;
    line-height: 1.2;
    letter-spacing: 4px;
    text-transform: uppercase;
  }
  .provider-name {
    top: 286px;
    font-family: "Open Sans", sans-serif;
    font-weight: 700;
    font-size: 21px;
  }
  .provider-email {
    top: 320px;
    font-family: "Open Sans", sans-serif;
    font-weight: 400;
    font-size: 20px;
  }
  .tagline {
    top: 414px;
    font-family: "Quicksand", sans-serif;
    font-weight: 400;
    font-size: 22px;
    letter-spacing: 2px;
  }
</style>
</head>
<body>
  <main class="canvas">
    <article class="business-card card-back" aria-label="Card back">
      <div class="back-content">
        <svg class="back-mark" viewBox="0 0 120 120" aria-hidden="true">
          <circle cx="60" cy="60" r="52" fill="none" stroke="var(--on-back)" stroke-width="4"/>
        </svg>
        <p class="back-name">Tolvery<br>Anesthesia LLC</p>
      </div>
    </article>

    <article class="business-card card-front" aria-label="Card front">
      <div class="bloom-decoration" role="img" aria-label="Large faint pink looping flower decoration"></div>
      <div class="front-content">
        <svg class="brand-mark" viewBox="0 0 120 120" aria-hidden="true">
          <circle cx="60" cy="60" r="52" fill="none" stroke="var(--brand-magenta)" stroke-width="5"/>
        </svg>
        <p class="brand-name">Tolvery<br>Anesthesia LLC</p>
        <p class="provider-name">Dr. Lisbeth Tolvery, CRNA, DNAP</p>
        <p class="provider-email">tolvery.anesthesia@quillmail.net</p>
        <p class="tagline">Keeping you safe and comfortable</p>
      </div>
    </article>
  </main>
</body>
</html>
```